Vextamine™

I need a product label for a 100 ml clear glass vial with a white, blue or red crimp top . The label dimensions are 2" x 6". I am attaching my rough draft, as well as some other art work that might help the designer have a more insight as to what I am seeking. Our printer needs the artwork to be 600x600dpi in resolution. I am open to the idea of our company logo "northbay biolabs" and the product name "VEXTAMINE™" being in chrome. This product is a site enhancement oil for bodybuilders. I prefer a more "pharma" style look over a gimmicky bodybuilder theme, BUT I am open to anyone's suggestions. After this is concluded, We also want to use the template for the remainder of our supplement line.We will obviously work with the same designer to complete the remaining 6-8 products. I am new to this so if there is anything you need from me to clarify from me, please ask :)

```html
<!DOCTYPE html>
<html lang="en">
<head>
<meta charset="utf-8">
<title>Vextamine™ Vial Label</title>
<link rel="stylesheet" href="https://fonts.googleapis.com/css2?family=Raleway:wght@400;500;700;800&display=swap">
<style>
  :root {
    --paper: #ffffff;
    --mint: #b1e0cd;
    --band: #449f7f;
    --trim: #e0227a;
    --ink: #111111;
    --white: #ffffff;
    --crop: #222222;
  }
  html, body {
    margin: 0;
    padding: 0;
    width: 1200px;
    height: 545px;
    overflow: hidden;
    background: var(--paper);
  }
  .canvas {
    position: relative;
    width: 1200px;
    height: 545px;
    font-family: "Raleway", sans-serif;
    color: var(--ink);
  }
  .label-bleed {
    position: absolute;
    left: 54px; top: 78px;
    width: 1084px; height: 391px;
    background: var(--mint);
  }
  .label-band {
    position: absolute;
    left: 54px; top: 361px;
    width: 1084px; height: 108px;
    background: var(--band);
  }
  .trim-line {
    position: absolute;
    left: 76px; top: 101px;
    width: 1038px; height: 343px;
    border: 1.5px solid var(--trim);
  }
  .crop-marks {
    position: absolute;
    left: 0; top: 0;
  }
  .text {
    position: absolute;
    margin: 0;
    white-space: nowrap;
  }
  .center { transform: translateX(-50%); text-align: center; }

  .features-brand { left: 232px; top: 130px; font-size: 22px; font-weight: 500; }
  .features-product { left: 232px; top: 156px; font-size: 27px; font-weight: 800; }
  .features-title { left: 232px; top: 186px; font-size: 20px; font-weight: 700; }
  .feature-list { position: absolute; left: 0; top: 0; margin: 0; padding: 0; list-style: none; }
  .feature {
    position: absolute;
    font-size: 22px;
    font-weight: 400;
    white-space: nowrap;
  }
  .feature::before {
    content: "";
    display: inline-block;
    width: 4px; height: 4px;
    background: var(--ink);
    margin-right: 14px;
    vertical-align: middle;
    position: relative;
    top: -4px;
  }
  .feature-1 { left: 108px; top: 241px; }
  .feature-2 { left: 124px; top: 284px; }
  .feature-3 { left: 152px; top: 328px; }

  .brand-mark {
    position: absolute;
    left: 596px; top: 146px;
    transform: translateX(-50%);
    display: flex;
    align-items: center;
    gap: 10px;
    font-size: 22px;
    font-weight: 800;
    letter-spacing: 2px;
    color: var(--ink);
    white-space: nowrap;
  }
  .brand-dot {
    width: 14px; height: 14px;
    border-radius: 50%;
    background: var(--ink);
  }
  .product-name { left: 596px; top: 232px; font-size: 34px; font-weight: 700; }
  .grade { left: 596px; top: 311px; font-size: 26px; font-weight: 400; }
  .contents { left: 596px; top: 404px; font-size: 26px; font-weight: 400; color: var(--white); }

  .instructions-title { left: 974px; top: 130px; font-size: 24px; font-weight: 500; }
  .instructions-text { left: 974px; top: 183px; font-size: 21px; font-weight: 400; }
  .shake-illustration {
    position: absolute;
    left: 948px; top: 236px;
    width: 72px; height: 120px;
    background: linear-gradient(180deg, #9fd2bd, #8cc6ae);
    border-radius: 6px;
  }
  .shake-badge {
    position: absolute;
    left: 974px; top: 369px;
    transform: translateX(-50%);
    display: flex;
    align-items: center;
    gap: 6px;
    color: var(--white);
  }
  .shake-badge svg { display: block; }
  .shake-words { text-align: center; line-height: 1; }
  .shake-main { display: block; font-size: 16px; font-weight: 800; }
  .shake-sub { display: block; font-size: 13px; font-weight: 500; letter-spacing: 0.5px; margin-top: 4px; }
</style>
</head>
<body>
<div class="canvas">
  <svg class="crop-marks" width="1200" height="545" viewBox="0 0 1200 545" aria-hidden="true">
    <g stroke="var(--crop)" stroke-width="1.2">
      <line x1="76" y1="24" x2="76" y2="84"/>
      <line x1="1116" y1="24" x2="1116" y2="84"/>
      <line x1="76" y1="462" x2="76" y2="521"/>
      <line x1="1116" y1="462" x2="1116" y2="521"/>
      <line x1="0" y1="101" x2="60" y2="101"/>
      <line x1="1138" y1="101" x2="1200" y2="101"/>
      <line x1="0" y1="446" x2="60" y2="446"/>
      <line x1="1138" y1="446" x2="1200" y2="446"/>
    </g>
  </svg>

  <div class="label-bleed" role="img" aria-label="Soft mint background with a faint molecular hexagon pattern"></div>
  <div class="label-band"></div>
  <div class="trim-line"></div>

  <p class="text center features-brand">Northbay Biolabs’s</p>
  <p class="text center features-product">VEXTAMINE</p>
  <p class="text center features-title">Features:</p>
  <ul class="feature-list">
    <li class="feature feature-1">Muscle Volumization</li>
    <li class="feature feature-2">Site Enhancement</li>
    <li class="feature feature-3">Join Therapy</li>
  </ul>

  <div class="brand-mark"><span class="brand-dot"></span><span>NORTHBAY BIOLABS</span></div>
  <h1 class="text center product-name">VEXTAMINE™</h1>
  <p class="text center grade">Pharmaceutical Grade</p>
  <p class="text center contents">Contents: 100 ml</p>

  <h2 class="text center instructions-title">Instructions:</h2>
  <p class="text center instructions-text">Shake before use.</p>
  <div class="shake-illustration" role="img" aria-label="Line icon of a hand shaking a bottle"></div>
  <div class="shake-badge">
    <svg width="10" height="22" viewBox="0 0 10 22" aria-hidden="true"><polygon points="10,0 0,11 10,22" fill="var(--white)"/></svg>
    <div class="shake-words">
      <span class="shake-main">SHAKE WELL</span>
      <span class="shake-sub">BEFORE USING</span>
    </div>
    <svg width="10" height="22" viewBox="0 0 10 22" aria-hidden="true"><polygon points="0,0 10,11 0,22" fill="var(--white)"/></svg>
  </div>
</div>
</body>
</html>
```